Sales and Lettings Boards

Hello, please see attached our sales and lettings boards for our estate agency. These were "designed" by the sign writers. As you can see they are pretty flat and boring - could you work your magic and make them stand out please? I've also attached the logo files. Many thanks, Dean

Target Market(s)

Consumers - residential sale property sales and lettings

Industry/Entity Type

Real Estate Agent

```html
<!DOCTYPE html>
<html lang="en">
<head>
<meta charset="utf-8">
<title>Novara Sales &amp; Lettings – For Sale Board</title>
<link rel="stylesheet" href="https://fonts.googleapis.com/css2?family=Open+Sans:wght@700&family=Poppins:wght@500;600&display=swap">
<style>
  :root {
    --band-green: #62b94a;
    --band-yellow: #fdc20b;
    --band-orange: #fb6321;
    --brand-dark: #4b4b4d;
    --white: #ffffff;
    --tag-soft: #fff6dc;
    --tag-letter: #f4692c;
    --phone-icon: #fca586;
    --url-pill: #fdb596;
    --url-text: #1e1e1e;
    --skyline-a: rgba(120, 200, 100, 0.0);
    --skyline-b: rgba(150, 215, 125, 0.55);
  }
  html, body {
    margin: 0;
    padding: 0;
    width: 1200px;
    height: 959px;
    overflow: hidden;
    background: var(--white);
  }
  .board {
    display: block;
    width: 1200px;
    height: 959px;
    font-family: "Poppins", Arial, sans-serif;
  }
  .band-brand { fill: var(--band-green); }
  .band-status { fill: var(--band-yellow); }
  .band-contact { fill: var(--band-orange); }
  .brand-name { fill: var(--brand-dark); font-weight: 600; font-size: 104px; }
  .brand-tagline { fill: var(--white); font-weight: 500; font-size: 46px; }
  .status-for { fill: var(--white); font-weight: 600; font-size: 116px; }
  .tag-letter { fill: var(--tag-letter); font-weight: 600; font-size: 118px; text-anchor: middle; }
  .phone-icon { fill: var(--phone-icon); }
  .phone-number { fill: var(--white); font-family: "Open Sans", Arial, sans-serif; font-weight: 700; font-size: 78px; }
  .url-pill { fill: var(--url-pill); }
  .url-text { fill: var(--url-text); font-family: "Open Sans", Arial, sans-serif; font-weight: 700; font-size: 30px; }
</style>
</head>
<body>
<svg class="board" viewBox="0 0 1000 799" xmlns="http://www.w3.org/2000/svg">
  <defs>
    <linearGradient id="skyline-fill" x1="0" y1="0" x2="0" y2="1">
      <stop offset="0" stop-color="var(--skyline-a)"/>
      <stop offset="1" stop-color="var(--skyline-b)"/>
    </linearGradient>
    <linearGradient id="tags-fill" x1="0" y1="0" x2="0" y2="1">
      <stop offset="0" stop-color="var(--white)"/>
      <stop offset="1" stop-color="var(--tag-soft)"/>
    </linearGradient>
  </defs>

  <!-- brand band -->
  <rect class="band-brand" x="0" y="0" width="1000" height="265"/>
  <rect class="skyline" role="img" aria-label="Faint city skyline with tower blocks and trees" x="440" y="70" width="560" height="195" fill="url(#skyline-fill)"/>
  <text class="brand-name" x="55" y="135" textLength="423" lengthAdjust="spacing">NOVARA</text>
  <text class="brand-tagline" x="58" y="212" textLength="417" lengthAdjust="spacing">Sales &amp; Lettings</text>

  <!-- status band -->
  <rect class="band-status" x="0" y="265" width="1000" height="266"/>
  <text class="status-for" x="52" y="452" textLength="166" lengthAdjust="spacingAndGlyphs">For</text>

  <rect class="sale-tags" role="img" aria-label="Four white price tags hanging on strings" x="290" y="290" width="615" height="230" rx="10" fill="url(#tags-fill)"/>
  <g class="sale-word">
    <text class="tag-letter" x="350" y="462">S</text>
    <text class="tag-letter" x="515" y="462">A</text>
    <text class="tag-letter" x="672" y="462">L</text>
    <text class="tag-letter" x="843" y="462">E</text>
  </g>

  <!-- contact band -->
  <rect class="band-contact" x="0" y="531" width="1000" height="268"/>
  <path class="phone-icon" transform="translate(88 588) scale(7)" d="M6.62 10.79c1.44 2.83 3.76 5.14 6.59 6.59l2.2-2.2c.27-.27.67-.36 1.02-.24 1.12.37 2.33.57 3.57.57.55 0 1 .45 1 1V20c0 .55-.45 1-1 1-9.39 0-17-7.61-17-17 0-.55.45-1 1-1h3.5c.55 0 1 .45 1 1 0 1.25.2 2.45.57 3.57.11.35.03.74-.25 1.02l-2.2 2.2z"/>
  <text class="phone-number" x="327" y="667" textLength="499" lengthAdjust="spacing">01632 960418</text>

  <path class="url-pill" d="M562,736 H1000 V799 H542 V756 Q542,736 562,736 Z"/>
  <text class="url-text" x="567" y="779" textLength="408" lengthAdjust="spacingAndGlyphs">www.novara-estates.co.uk</text>
</svg>
</body>
</html>
```